Baby Shower Invitation for Vectored Image Provided

Delphine & Gerald's Baby Shower - Black/White/Gold Colors preferred
Please use the vectored portrait image attached. I'd like us on the lower right side of the invitation.
Can be horizontal or vertical layout.
The second image attached has the information needed for you to complete.
I don't want that style copied, it is just an example.

```html
<!DOCTYPE html>
<html lang="en">
<head>
<meta charset="utf-8">
<title>Oh Boy! Baby Shower Invitation</title>
<link rel="stylesheet" href="https://fonts.googleapis.com/css2?family=Archivo:wght@700;800&family=Crimson+Text:wght@400&family=Playball&display=swap">
<style>
  :root {
    --backdrop: #e9e7e3;
    --ink: #0d0d0d;
    --stripe: #ffffff;
    --gold-light: #f4d88f;
    --gold-mid: #d9a542;
    --gold-deep: #a8681c;
    --bronze: #5a2e12;
    --script-fill: #ffffff;
    --portrait-dark: #1c1714;
    --portrait-warm: #8a5a3c;
  }
  * { margin: 0; padding: 0; box-sizing: border-box; }
  html, body { width: 1200px; height: 899px; overflow: hidden; background: var(--backdrop); }
  .invitation {
    position: absolute; left: 296px; top: 20px; width: 609px; height: 860px;
    background: var(--ink); overflow: hidden;
  }
  .stripes {
    position: absolute; left: 18px; top: 18px; right: 18px; bottom: 18px;
    background: repeating-linear-gradient(-32deg, var(--stripe) 0 30px, var(--ink) 30px 62px);
  }
  .plaque { position: absolute; left: 82px; top: 115px; width: 438px; height: 636px; }
  .line { position: absolute; left: 0; width: 100%; text-align: center; color: var(--ink); white-space: nowrap; }
  .crown { position: absolute; left: 318px; top: 160px; width: 26px; height: 20px; }
  .headline-script {
    position: absolute; left: 0; width: 100%; text-align: center;
    font-family: "Playball", cursive; color: var(--script-fill);
    -webkit-text-stroke: 1.5px var(--bronze); paint-order: stroke fill;
    text-shadow: 1px 1px 0 var(--bronze);
  }
  .oh-boy { top: 182px; left: 8px; font-size: 60px; line-height: 1; }
  .tagline { font-family: "Archivo", sans-serif; font-weight: 800; font-size: 28px; line-height: 33px; top: 266px; left: 8px; }
  .serif { font-family: "Crimson Text", serif; font-size: 17px; line-height: 22px; }
  .intro { top: 333px; left: 8px; }
  .guest-name { top: 388px; left: 8px; font-size: 36px; line-height: 1; }
  .rule { position: absolute; border-top: 1.5px dotted #3a2410; }
  .rule-v { position: absolute; border-left: 1.5px dotted #3a2410; }
  .weekday {
    position: absolute; left: 158px; top: 500px; font-family: "Crimson Text", serif; font-size: 21px;
    transform: rotate(-90deg); transform-origin: left top; color: var(--ink);
  }
  .month { position: absolute; left: 194px; top: 454px; font-family: "Archivo", sans-serif; font-weight: 800; font-size: 29px; color: var(--ink); }
  .day { position: absolute; left: 216px; top: 484px; font-family: "Archivo", sans-serif; font-weight: 800; font-size: 54px; line-height: 1; color: var(--ink); }
  .details { position: absolute; left: 291px; width: 162px; text-align: center; color: var(--ink); font-family: "Crimson Text", serif; }
  .time { top: 446px; font-size: 19px; }
  .venue { top: 482px; font-size: 17px; line-height: 22px; }
  .rsvp { top: 558px; left: 8px; }
  .registry-script {
    position: absolute; left: 8px; width: 100%; text-align: center;
    font-family: "Playball", cursive; color: var(--ink); font-size: 22px; line-height: 31px; top: 614px;
  }
  .portrait {
    position: absolute; left: 377px; top: 525px; width: 217px; height: 317px;
    background: radial-gradient(ellipse at 70% 30%, var(--portrait-warm) 0%, var(--portrait-dark) 70%);
    clip-path: polygon(45% 0, 100% 0, 100% 100%, 0 100%, 0 52%, 45% 52%);
  }
</style>
</head>
<body>
  <main class="invitation">
    <div class="stripes"></div>

    <svg class="plaque" viewBox="0 0 438 636" aria-hidden="true">
      <defs>
        <linearGradient id="goldSheen" x1="0" y1="0" x2="1" y2="0.3">
          <stop offset="0" stop-color="#b9782a"/>
          <stop offset="0.3" stop-color="#f4d88f"/>
          <stop offset="0.6" stop-color="#d9a542"/>
          <stop offset="1" stop-color="#a8681c"/>
        </linearGradient>
      </defs>
      <path d="M40,40 C110,45 170,20 219,8 C268,20 328,45 398,40 C392,70 405,90 430,100 C420,250 420,386 430,536 C405,546 392,566 398,596 C328,591 268,616 219,628 C170,616 110,591 40,596 C46,566 33,546 8,536 C18,386 18,250 8,100 C33,90 46,70 40,40 Z"
            fill="url(#goldSheen)" stroke="#f6e2a8" stroke-width="8"/>
      <path d="M40,40 C110,45 170,20 219,8 C268,20 328,45 398,40 C392,70 405,90 430,100 C420,250 420,386 430,536 C405,546 392,566 398,596 C328,591 268,616 219,628 C170,616 110,591 40,596 C46,566 33,546 8,536 C18,386 18,250 8,100 C33,90 46,70 40,40 Z"
            fill="none" stroke="#5a2e12" stroke-width="3" transform="translate(219 318) scale(0.97) translate(-219 -318)"/>
    </svg>

    <svg class="crown" viewBox="0 0 26 20" aria-hidden="true">
      <path d="M2,17 L1,5 L7,10 L13,2 L19,10 L25,5 L24,17 Z" fill="#0d0d0d"/>
      <circle cx="1" cy="4" r="1.6" fill="#0d0d0d"/><circle cx="13" cy="2" r="1.6" fill="#0d0d0d"/><circle cx="25" cy="4" r="1.6" fill="#0d0d0d"/>
    </svg>

    <h1 class="headline-script oh-boy">Oh Boy!</h1>
    <p class="line tagline">A LITTLE MAN<br>IS ON THE WAY!</p>
    <p class="line serif intro">Please join us for a<br>Baby Shower honoring</p>
    <p class="headline-script guest-name">Delphine Marlowe</p>

    <div class="rule" style="left:155px; top:441px; width:296px;"></div>
    <div class="rule-v" style="left:289px; top:443px; height:110px;"></div>
    <p class="weekday">Saturday</p>
    <p class="month">SEPT</p>
    <p class="day">1</p>
    <p class="details time">11:30am-2:30pm</p>
    <div class="rule" style="left:289px; top:477px; width:162px;"></div>
    <p class="details venue">The Willowmere<br>1847 Ashford Ln.<br>Raleigh, NC</p>
    <div class="rule" style="left:155px; top:553px; width:296px;"></div>
    <p class="line serif rsvp">RSVP to Gerald at 919-555-0143<br>by August 20th</p>
    <div class="rule" style="left:155px; top:608px; width:296px;"></div>
    <p class="registry-script">Delphine is registered at<br>Cradle &amp; Co.</p>

    <div class="portrait" role="img" aria-label="Vector portrait of the expecting couple, Delphine and Gerald, standing together in black outfits"></div>
  </main>
</body>
</html>
```